Export company based in South America (Ecuador) we export flowers, chocolate, and bananas

We need a website that gives our potential clients and introduction into our company and the different types of commodities we export around the world. We are based in Quito, Ecuador so the website should portray the feel of Ecuadorian landscapes within a modern looking website.
At the moment we are exporting roses, chocolate, and bananas so the website should have an intro to our company and then three different areas that describe our three main commodity. The three different sections should explain why each of the products from Ecuador are some of the best in the world in their categories and the benefits of importing the commodity through our company.
Industry/Entity Type
Commodity
Number of Pages Required
4 page

```html
<!DOCTYPE html>
<html lang="en">
<head>
<meta charset="utf-8">
<title>Andeva Exports</title>
<link href="https://fonts.googleapis.com/css2?family=Poppins:ital,wght@0,300;0,400;0,500;0,600;0,700;0,800;0,900;1,500&display=swap" rel="stylesheet">
<style>
:root{
  --gold:#e2a806;
  --ink:#222222;
  --text:#2b2b2b;
  --muted:#f4f4f4;
  --line:#d8d8d8;
  --navy:#1c2541;
}
*{margin:0;padding:0;box-sizing:border-box}
html,body{width:1200px;height:2710px;overflow:hidden;background:#fff}
body{font-family:'Poppins',sans-serif;color:var(--text);position:relative}
.abs{position:absolute}
.brand{left:66px;top:14px;font-size:34px;font-weight:800;color:var(--gold);letter-spacing:-0.5px}
.nav a{position:absolute;top:27px;font-size:14px;color:var(--ink);text-decoration:none}
.search{left:923px;top:15px;width:210px;height:40px;border:1px solid var(--line);border-radius:20px;background:#f6f6f6}
.search span{position:absolute;left:16px;top:11px;font-size:12px;color:#999}
.search .divider{position:absolute;left:170px;top:11px;width:1px;height:18px;background:#ccc}
.search svg{position:absolute;left:180px;top:12px}
.hero{left:66px;top:74px;width:1067px;height:555px;background:linear-gradient(180deg,#8ccbef 0%,#6aa3d4 25%,#3f5d7d 45%,#2f3b2e 65%,#1c2230 100%)}
.hero-small{left:124px;top:385px;font-size:37px;font-weight:500;color:#fff}
.hero-big{left:118px;top:380px;font-size:158px;font-weight:800;color:#fff;letter-spacing:-3px;line-height:1.2}
.photo{position:absolute}
.sq{position:absolute}
.eyebrow{left:622px;top:812px;font-size:25px;font-weight:700;color:var(--gold)}
.h-company{left:620px;top:838px;font-size:62px;font-weight:400;color:var(--ink);line-height:1.2}
.copy{font-size:14px;line-height:20px;color:var(--ink);font-weight:400}
.learn{font-size:13px;font-weight:600;color:var(--gold);display:flex;align-items:center;gap:10px}
.exports-band{left:0;top:1351px;width:1200px;height:973px;background:var(--muted)}
.h-exports{left:62px;top:1430px;font-size:150px;font-weight:300;color:var(--ink);line-height:1.2;letter-spacing:-1px}
.card-img{position:absolute;width:335px;height:335px;top:1784px}
.card-title{position:absolute;top:2136px;font-size:28px;font-weight:300;color:var(--ink)}
.card-copy{position:absolute;top:2180px;width:335px;font-size:12px;line-height:18px;color:var(--ink)}
.card-arrow{position:absolute;top:2232px}
.contact{left:66px;top:2324px;width:1067px;height:334px;background:var(--gold)}
.h-contact{left:128px;top:2378px;font-size:64px;font-weight:400;color:var(--ink);line-height:1.2}
.info{position:absolute;top:2550px;display:flex;gap:10px}
.info small{display:block;font-size:12px;color:var(--navy)}
.info strong{display:block;font-size:18px;font-weight:700;color:var(--navy);line-height:18px}
.info .addr{font-size:15px;line-height:16px}
.social{left:72px;top:2674px;display:flex;gap:14px}
.social span{width:20px;height:20px;border-radius:50%;background:var(--navy);display:block}
.copyright{right:76px;top:2676px;font-size:13.5px;font-style:italic;font-weight:500;color:var(--navy)}
</style>
</head>
<body>

<header>
  <div class="abs brand">andeva</div>
  <nav class="nav">
    <a style="left:408px" href="#">Home</a>
    <a style="left:504px" href="#">Company</a>
    <a style="left:620px" href="#">Exports</a>
    <a style="left:717px" href="#">Contact Us</a>
  </nav>
  <div class="abs search">
    <span>Search</span><i class="divider"></i>
    <svg width="14" height="14" viewBox="0 0 14 14" fill="none" stroke="#999" stroke-width="1.3"><circle cx="6" cy="6" r="4.5"/><line x1="9.3" y1="9.3" x2="13" y2="13"/></svg>
  </div>
</header>

<section>
  <div class="abs hero" role="img" aria-label="Snow-capped volcano above a hillside city with a winged statue at dusk"></div>
  <div class="abs hero-small">welcome to</div>
  <div class="abs hero-big">ecuador</div>
</section>

<section class="about">
  <div class="sq" style="left:359px;top:749px;width:22px;height:23px;background:var(--ink)"></div>
  <div class="photo" style="left:103px;top:772px;width:255px;height:255px;background:linear-gradient(180deg,#c9d6e0 0%,#6f8a3a 45%,#b4502e 80%,#5a3a20 100%)" role="img" aria-label="Garden of flowers in front of a stone tower"></div>
  <div class="photo" style="left:359px;top:772px;width:149px;height:151px;background:linear-gradient(135deg,#d8d8d8,#444 55%,#1e1e1e)" role="img" aria-label="Stack of dark chocolate pieces"></div>
  <div class="sq" style="left:508px;top:923px;width:18px;height:19px;background:var(--gold)"></div>
  <div class="sq" style="left:66px;top:1027px;width:39px;height:39px;background:var(--gold)"></div>
  <div class="photo" style="left:216px;top:1028px;width:142px;height:141px;background:linear-gradient(135deg,#7a4a32,#4a2a1c 60%,#b57a5a)" role="img" aria-label="Hands holding cocoa beans"></div>
  <div class="photo" style="left:359px;top:1028px;width:204px;height:203px;background:linear-gradient(180deg,#8fcf6a,#3f8a2a 55%,#2f4a22)" role="img" aria-label="Banana plants in a plantation"></div>
  <div class="sq" style="left:198px;top:1170px;width:18px;height:18px;background:#c9c9c9"></div>

  <div class="abs eyebrow">About</div>
  <h2 class="abs h-company">Company</h2>
  <p class="abs copy" style="left:617px;top:941px;width:490px">nally aggregate distinctive deliverables with global outsourcing. Uniquely strategize professional technology via enabled content.</p>
  <p class="abs copy" style="left:617px;top:1001px;width:490px">Compellingly customize innovative quality vectors with revolutionary outsourcing. Monotonectally underwhelm multidisciplinary resources with interactive testing procedures. Conveniently communicate client-centered initiatives without transparent e-services. Appropriately drive efficient innovation vis-a-vis open-source human capital. Progressively monetize ethical technology and team driven manufactured products.</p>
  <div class="abs learn" style="left:617px;top:1169px">Learn More
    <svg width="26" height="10" viewBox="0 0 26 10" fill="none" stroke="#e2a806" stroke-width="1.5"><line x1="0" y1="5" x2="24" y2="5"/><polyline points="19,1 24,5 19,9"/></svg>
  </div>
</section>

<section class="exports">
  <div class="abs exports-band"></div>
  <h2 class="abs h-exports">Exports</h2>
  <div class="abs learn" style="left:625px;top:1555px">Learn More
    <svg width="26" height="10" viewBox="0 0 26 10" fill="none" stroke="#e2a806" stroke-width="1.5"><line x1="0" y1="5" x2="24" y2="5"/><polyline points="19,1 24,5 19,9"/></svg>
  </div>
  <p class="abs copy" style="left:82px;top:1631px;width:940px">nally aggregate distinctive deliverables with global outsourcing. Uniquely strategize professional technology via enabled content.</p>
  <p class="abs copy" style="left:82px;top:1671px;width:940px">Compellingly customize innovative quality vectors with revolutionary outsourcing. Monotonectally underwhelm multidisciplinary resources with interactive testing procedures. Conveniently communicate client</p>

  <div class="card-img" style="left:66px;background:linear-gradient(135deg,#9a6e5c,#6a4a3c 50%,#2a2422 75%,#e8e2dc)" role="img" aria-label="Pile of cocoa beans in a dark bowl"></div>
  <div class="card-img" style="left:432px;background:linear-gradient(180deg,#4f7a2e,#3a6a22 45%,#5cae2e 80%,#7acb3a)" role="img" aria-label="Rows of banana trees on green hills"></div>
  <div class="card-img" style="left:799px;background:radial-gradient(circle at 70% 30%,#f09a1c 0%,#d8501a 14%,#6aa62a 32%,#3e7a1e 100%)" role="img" aria-label="Orange and yellow rose in bloom"></div>

  <h3 class="card-title" style="left:66px">chocolate</h3>
  <h3 class="card-title" style="left:432px">Banana</h3>
  <h3 class="card-title" style="left:799px">Roses</h3>
  <p class="card-copy" style="left:66px">Compellingly customize innovative quality vectors with revolutionary outsourcing. Monotonectally</p>
  <p class="card-copy" style="left:432px">Compellingly customize innovative quality vectors with revolutionary outsourcing. Monotonectally</p>
  <p class="card-copy" style="left:799px">Compellingly customize innovative quality vectors with revolutionary outsourcing. Monotonectally</p>
  <svg class="card-arrow" style="left:66px" width="24" height="10" viewBox="0 0 24 10" fill="none" stroke="#e2a806" stroke-width="1.5"><line x1="0" y1="5" x2="22" y2="5"/><polyline points="17,1 22,5 17,9"/></svg>
  <svg class="card-arrow" style="left:432px" width="24" height="10" viewBox="0 0 24 10" fill="none" stroke="#e2a806" stroke-width="1.5"><line x1="0" y1="5" x2="22" y2="5"/><polyline points="17,1 22,5 17,9"/></svg>
  <svg class="card-arrow" style="left:799px" width="24" height="10" viewBox="0 0 24 10" fill="none" stroke="#e2a806" stroke-width="1.5"><line x1="0" y1="5" x2="22" y2="5"/><polyline points="17,1 22,5 17,9"/></svg>
</section>

<section>
  <div class="abs contact"></div>
  <h2 class="abs h-contact">Contact Us</h2>
  <p class="abs copy" style="left:128px;top:2471px;width:930px;font-size:14.5px">Compellingly customize innovative quality vectors with revolutionary outsourcing. Monotonectally underwhelm multidisciplinary resources with interactive testing procedures. Conveniently communicate client-centered initiatives without transparent</p>

  <div class="info" style="left:128px">
    <svg width="24" height="24" viewBox="0 0 24 24" fill="#1c2541" style="margin-top:8px"><path d="M6.6 10.8c1.4 2.8 3.8 5.1 6.6 6.6l2.2-2.2c.3-.3.7-.4 1-.2 1.1.4 2.3.6 3.6.6.6 0 1 .4 1 1V20c0 .6-.4 1-1 1C10.6 21 3 13.4 3 4c0-.6.4-1 1-1h3.5c.6 0 1 .4 1 1 0 1.3.2 2.5.6 3.6.1.3 0 .7-.2 1z"/></svg>
    <div><small>Phone</small><strong>0123 456 789 0011</strong></div>
  </div>
  <div class="info" style="left:404px">
    <svg width="24" height="24" viewBox="0 0 24 24" fill="#1c2541" style="margin-top:8px"><path d="M2 5h20v14H2z M3.5 6.5 12 13l8.5-6.5" stroke="#e2a806" stroke-width="1.5"/></svg>
    <div><small>Mail</small><strong>info@andeva.com</strong></div>
  </div>
  <div class="info" style="left:686px">
    <svg width="22" height="30" viewBox="0 0 22 30" fill="#1c2541" style="margin-top:4px"><path d="M11 0C5 0 0 4.8 0 10.8 0 18.5 11 30 11 30s11-11.5 11-19.2C22 4.8 17 0 11 0zm0 15a4.2 4.2 0 1 1 0-8.4 4.2 4.2 0 0 1 0 8.4z"/></svg>
    <div style="width:280px"><small>Address</small><strong class="addr">48 Calle Los Alamos, Quito Norte,</strong></div>
  </div>
</section>

<footer>
  <div class="abs social"><span></span><span></span><span></span><span></span></div>
  <div class="abs copyright">2019 - 2020 © Andeva.com - Copyright All Rights Reserved</div>
</footer>

</body>
</html>
```